2 page brouchure for a Property Valuation company.

We require a 2 page brochure (printed front and back) for a property valuation company known as 'Brookmere Valuations'.

Brookmere valuations provides independent, reliable, accurate valuation services to our clients on the value of their properties to enable confidence and certainty in their decision.

The brochure is to be used to convey that the company provides valuation services for 8 main purposes and across 4 different property types.

The 8 main purposes for valuation include:
- Pre-Purchase Valuations
- Stamp Duty Valuations
-Capital Gains Tax (CGT)Valuations
-Unit Entitlement Valuations
-Family Law and Litigation Valuations
-Easement Valuations
-Wills & Probate Valuations
-Insolvency/Asset Realisation Valuations

The 4 main property types are:
-Residential
-Commercial
-Industrial
-Retail.

The brochure should have a title page, a page for the services, a page for the property types and a rear page with contact details.
Contact detail will include;
email:
phone :
Post :
website:

The words 'property valuation and advisory services' should be used at the front of the brochure.

The brochure should be professional and is used to convey information using visual aid and is to be used for promotion.

Our main colors are dark green and grey as seen in our logo.

We have attached our logo to add to the brochure and visit our website at: www.brookmerevaluations-example.com.au for more information about the company.

Please let me know if there are any further questions.

Target Market(s)

Solicitors/Lawyers
Accountants
Surveyors
Builders/Developers

Requirements
Must have
• Logo Colors, Logo, 8 Main services, 4 main property types, contact details.
Nice to have
• Should have concise visual aids to convey message.

Please add that we provide fast 48 hour turnaround for short form valuations. Maybe use a visual aid to convey this.

```html
<!DOCTYPE html>
<html lang="en">
<head>
<meta charset="utf-8">
<title>Brookmere Valuations – Brochure</title>
<link href="https://fonts.googleapis.com/css2?family=Archivo+Black&family=Arimo:wght@400;700&display=swap" rel="stylesheet">
<style>
:root{
  --green:#0b6b3a;
  --green-dark:#07522c;
  --charcoal:#3b3b3d;
  --text:#1d1d1d;
  --grey:#8a8a8a;
  --rule:#c9c9c9;
  --stage:#5f6b6a;
  --paper:#ffffff;
  --spine:#d9d9d9;
}
*{box-sizing:border-box;margin:0;padding:0}
html,body{width:1200px;height:2400px;overflow:hidden}
body{background:var(--stage);font-family:"Arimo",Arial,sans-serif;color:var(--text);position:relative}
.spread{position:absolute;left:30px;width:1140px;height:880px}
.spread--outer{top:320px}
.spread--inner{top:1240px}
.page{position:absolute;top:0;width:570px;height:880px;overflow:hidden;background:var(--paper)}
.page--left{left:0}
.page--right{left:570px;background:linear-gradient(90deg,var(--spine) 0%,#f4f4f4 12%,#fff 30%)}
.abs{position:absolute}
.photo{position:absolute}
.brand{position:absolute;display:flex;align-items:center;gap:14px}
.brand__mark{background:var(--green);flex:none}
.brand__name{font-family:"Arimo",Arial,sans-serif;font-weight:400;color:var(--charcoal);text-transform:uppercase;line-height:1.15;white-space:nowrap}

/* back page */
.call{position:absolute;left:107px;top:365px;width:360px}
.call__label{height:32px;background:var(--green);border-radius:0 18px 0 0;color:#fff;font-family:"Archivo Black",sans-serif;font-size:17px;letter-spacing:7px;display:flex;align-items:center;padding-left:40px}
.call__number{height:68px;background:var(--charcoal);border-radius:0 0 0 22px;color:#fff;font-size:36px;display:flex;align-items:center;gap:14px;padding-left:36px}
.turnaround{position:absolute;left:107px;top:500px;width:360px;display:flex;align-items:center;gap:14px}
.turnaround__badge{width:74px;height:74px;flex:none}
.turnaround__text{font-size:13px;line-height:17px;color:var(--charcoal);text-transform:uppercase}
.turnaround__text strong{display:block;color:var(--green);font-family:"Archivo Black",sans-serif;font-weight:400;font-size:16px;line-height:20px}
.contact{position:absolute;left:36px;top:733px;font-size:12.5px;color:var(--text)}
.contact li{list-style:none;display:flex;align-items:center;gap:7px;height:29px;white-space:nowrap}
.contact svg{flex:none}
.divider-v{position:absolute;left:330px;top:718px;width:3px;height:110px;background:var(--charcoal)}

/* cover */
.cover__band{left:235px;top:165px;width:335px;height:50px;background:#e1e1e1}
.cover__title{position:absolute;left:0;width:570px;top:650px;text-align:center;font-family:"Archivo Black",sans-serif;font-size:34px;line-height:36px;color:var(--green);text-transform:uppercase}
.cover__sub{position:absolute;left:0;width:570px;top:746px;text-align:center;font-size:14px;color:var(--charcoal);text-transform:uppercase}
.pill{position:absolute;left:62px;top:790px;width:450px;height:38px;border-radius:19px;background:var(--green);color:#fff;font-size:16px;letter-spacing:1.5px;display:flex;align-items:center;justify-content:center}

/* what we do */
.wwd__title{position:absolute;left:290px;top:58px;font-size:31px;color:var(--green);text-transform:uppercase}
.wwd__title b{font-family:"Archivo Black",sans-serif;font-weight:400}
.wwd__rule{left:290px;top:108px;width:242px;height:2px;background:var(--rule)}
.wwd__copy{position:absolute;left:290px;top:124px;width:242px;font-size:10.6px;line-height:13.6px;text-align:justify}
.wwd__copy p+p{margin-top:12px}
.purposes__head{position:absolute;left:0;width:570px;top:376px;text-align:center;color:var(--green);font-weight:700;font-size:12.5px;text-transform:uppercase}
.purposes__sub{position:absolute;left:0;width:570px;top:394px;text-align:center;font-size:15px}
.purpose{position:absolute;display:flex;align-items:center;gap:10px;font-size:14px;line-height:16px;text-transform:uppercase}
.purpose strong{color:var(--green);font-weight:700;display:block}
.icon-ring{width:36px;height:36px;flex:none}

/* property types */
.type__head{position:absolute;font-size:16px;color:var(--green);text-transform:uppercase;white-space:nowrap}
.type__head b{font-family:"Archivo Black",sans-serif;font-weight:400}
.type__rule{position:absolute;height:2px;background:var(--rule)}
.type__copy{position:absolute;width:229px;font-size:10.8px;line-height:13.5px;text-align:justify}
.bullets{position:absolute;display:grid;grid-template-columns:115px 115px;column-gap:4px;font-size:10.6px;line-height:12.6px;font-weight:700}
.bullets li{list-style:none;padding-left:13px;position:relative;margin-bottom:1px}
.bullets li::before{content:"";position:absolute;left:0;top:2px;width:8px;height:8px;border:2px solid currentColor;border-radius:2px}
.bullets .g{color:var(--green)}
.bullets .k{color:var(--text)}
.grid-rule-v{left:290px;top:30px;width:2px;height:820px;background:var(--rule)}
.grid-rule-h{left:30px;top:447px;width:515px;height:2px;background:var(--rule)}
</style>
</head>
<body>

<section class="spread spread--outer">
  <div class="page page--left back">
    <div class="call">
      <div class="call__label">CALL US TODAY!</div>
      <div class="call__number">
        <svg width="34" height="34" viewBox="0 0 34 34"><circle cx="17" cy="17" r="16" fill="#fff"/><path d="M11 9c1-1 2-1 3 0l2 3c.6 1 .3 1.8-.5 2.4l-1 .8c1 2.3 2.7 4 5 5l.8-1c.6-.8 1.4-1.1 2.4-.5l3 2c1 1 1 2 0 3l-1.5 1.5C20 27 7 14 9.5 10.5z" fill="#3b3b3d"/></svg>
        <span>1300 555 019</span>
      </div>
    </div>
    <div class="turnaround">
      <svg class="turnaround__badge" viewBox="0 0 74 74">
        <circle cx="37" cy="37" r="34" fill="none" stroke="#0b6b3a" stroke-width="4"/>
        <path d="M37 3 A34 34 0 0 1 71 37" fill="none" stroke="#3b3b3d" stroke-width="4"/>
        <text x="37" y="40" text-anchor="middle" font-family="Archivo Black, sans-serif" font-size="22" fill="#0b6b3a">48</text>
        <text x="37" y="55" text-anchor="middle" font-family="Arimo, Arial, sans-serif" font-weight="700" font-size="10" fill="#3b3b3d">HOURS</text>
      </svg>
      <p class="turnaround__text"><strong>Fast 48 hour turnaround</strong>for short form valuations</p>
    </div>
    <ul class="contact">
      <li><svg width="20" height="20" viewBox="0 0 20 20"><circle cx="10" cy="10" r="8.5" fill="none" stroke="#0b6b3a" stroke-width="1.6"/><rect x="5.5" y="7" width="9" height="6.5" fill="none" stroke="#0b6b3a" stroke-width="1.3"/><path d="M5.5 7l4.5 3.5L14.5 7" fill="none" stroke="#0b6b3a" stroke-width="1.3"/></svg>info@brookmerevaluations-example.com.au</li>
      <li><svg width="20" height="20" viewBox="0 0 20 20"><circle cx="10" cy="10" r="8.5" fill="none" stroke="#0b6b3a" stroke-width="1.6"/><path d="M10 15.5s-4-4-4-7a4 4 0 018 0c0 3-4 7-4 7z" fill="#0b6b3a"/><circle cx="10" cy="8.5" r="1.5" fill="#fff"/></svg>PO Box 418 Fernvale NSW 2999</li>
      <li><svg width="20" height="20" viewBox="0 0 20 20"><circle cx="10" cy="10" r="8.5" fill="none" stroke="#0b6b3a" stroke-width="1.6"/><circle cx="10" cy="10" r="5" fill="none" stroke="#0b6b3a" stroke-width="1.2"/><path d="M5 10h10M10 5c-2 3-2 7 0 10M10 5c2 3 2 7 0 10" fill="none" stroke="#0b6b3a" stroke-width="1.1"/></svg>www.brookmerevaluations-example.com.au</li>
    </ul>
    <div class="divider-v"></div>
    <div class="brand" style="left:350px;top:752px;gap:10px">
      <span class="brand__mark" style="width:40px;height:40px"></span>
      <span class="brand__name" style="font-size:16px;letter-spacing:2px">Brookmere<br>Valuations</span>
    </div>
  </div>

  <div class="page page--right cover">
    <div class="brand" style="left:130px;top:55px">
      <span class="brand__mark" style="width:62px;height:62px"></span>
      <span class="brand__name" style="font-size:26px;letter-spacing:4px">Brookmere<br>Valuations</span>
    </div>
    <div class="abs cover__band"></div>
    <div class="photo" role="img" aria-label="Family relaxing together on a lawn in front of a modern glass house" style="left:0;top:215px;width:570px;height:390px;background:linear-gradient(180deg,#b9c3c6 0%,#9aa6a4 45%,#7fa05a 70%,#4f8a2c 100%)"></div>
    <svg class="abs" style="left:0;top:150px" width="570" height="480" viewBox="0 0 570 480">
      <path d="M240 65 H500 Q535 65 535 100 V175" fill="none" stroke="#fff" stroke-width="12" stroke-linecap="round"/>
      <path d="M35 250 V335 Q35 375 75 375 H350" fill="none" stroke="#fff" stroke-width="12" stroke-linecap="round"/>
    </svg>
    <h1 class="cover__title">Property Valuation<br>and Advisory Services</h1>
    <p class="cover__sub">To individuals, investors, developers and organisations</p>
    <div class="pill">www.brookmerevaluations-example.com.au</div>
  </div>
</section>

<section class="spread spread--inner">
  <div class="page page--left services">
    <svg class="abs" style="left:0;top:0" width="570" height="360" viewBox="0 0 570 360">
      <path d="M33 33 H520 Q536 33 536 49 V72" fill="none" stroke="#0b6b3a" stroke-width="6"/>
      <path d="M36 290 V322 Q36 338 52 338 H536" fill="none" stroke="#0b6b3a" stroke-width="6"/>
    </svg>
    <div class="photo" role="img" aria-label="Hands presenting a small model house" style="left:50px;top:62px;width:230px;height:252px;background:linear-gradient(160deg,#5b5f66 0%,#8c8177 50%,#c7a57a 100%)"></div>
    <h2 class="wwd__title">What <b>We Do</b></h2>
    <div class="abs wwd__rule"></div>
    <div class="wwd__copy">
      <p>We provide property valuation and advisory services to individuals, investors, developers and organisations. Our experts are dedicated to providing high quality valuation advice for every purpose from stamp duty valuations to transactional advice.</p>
      <p>Our reliability and proficiency is underpinned by extensive industry experience, highly qualified valuers, independent outlook and direct and transparent advice which allow us to produce reliable market-leading valuation service across a wide range of property types including residential, commercial, retail and industrial.</p>
    </div>
    <p class="purposes__head">We provide valuation advisory for a wide range of purposes;</p>
    <p class="purposes__sub">most common purposes include:</p>

    <div class="purpose" style="left:33px;top:438px">
      <svg class="icon-ring" viewBox="0 0 36 36"><circle cx="18" cy="18" r="16" fill="none" stroke="#0b6b3a" stroke-width="2"/><path d="M10 18l8-7 8 7M12.5 16v9h11v-9" fill="none" stroke="#0b6b3a" stroke-width="2"/></svg>
      <span><strong>Pre-purchase and</strong>Pre-sale valuations</span>
    </div>
    <div class="purpose" style="left:33px;top:490px">
      <svg class="icon-ring" viewBox="0 0 36 36"><circle cx="18" cy="18" r="16" fill="none" stroke="#0b6b3a" stroke-width="2"/><ellipse cx="16" cy="12" rx="6" ry="2" fill="none" stroke="#0b6b3a" stroke-width="1.6"/><path d="M10 12v10c0 1 2.7 2 6 2M22 12v3" fill="none" stroke="#0b6b3a" stroke-width="1.6"/><circle cx="23" cy="22" r="4.5" fill="#0b6b3a"/></svg>
      <span><strong style="display:inline">Stamp duty</strong> valuations</span>
    </div>
    <div class="purpose" style="left:33px;top:536px">
      <svg class="icon-ring" viewBox="0 0 36 36"><circle cx="18" cy="18" r="16" fill="none" stroke="#0b6b3a" stroke-width="2"/><path d="M11 25V21M15 25V18M19 25V15M23 25V12" stroke="#0b6b3a" stroke-width="2.4"/></svg>
      <span><strong>Capital gains</strong>Tax valuations</span>
    </div>
    <div class="purpose" style="left:33px;top:590px">
      <svg class="icon-ring" viewBox="0 0 36 36"><circle cx="18" cy="18" r="16" fill="none" stroke="#0b6b3a" stroke-width="2"/><rect x="11" y="10" width="14" height="16" fill="none" stroke="#0b6b3a" stroke-width="1.6"/><path d="M11 15.5h14M11 20.5h14M15.7 10v16M20.3 10v16" stroke="#0b6b3a" stroke-width="1.2"/></svg>
      <span><strong>Unit entitlement</strong>Valuations</span>
    </div>

    <div class="photo" role="img" aria-label="Advisors reviewing charts and paperwork at a desk" style="left:285px;top:428px;width:250px;height:200px;background:linear-gradient(135deg,#4a3d33 0%,#b7ada2 55%,#e6e6e8 100%)"></div>
    <div class="photo" role="img" aria-label="Magnifying glass held over a small wooden house model" style="left:33px;top:647px;width:250px;height:199px;background:linear-gradient(135deg,#7a3a12 0%,#c46a2a 45%,#e5c9a6 100%)"></div>

    <div class="purpose" style="left:295px;top:665px">
      <svg class="icon-ring" viewBox="0 0 36 36"><circle cx="18" cy="18" r="16" fill="none" stroke="#0b6b3a" stroke-width="2"/><path d="M12 15l6-6 4 4-6 6zM17 17l7 7" stroke="#0b6b3a" stroke-width="2.2" fill="none"/><path d="M10 26h9" stroke="#0b6b3a" stroke-width="2"/></svg>
      <span><strong>Family law and</strong>Litigation valuations</span>
    </div>
    <div class="purpose" style="left:295px;top:718px">
      <svg class="icon-ring" viewBox="0 0 36 36"><circle cx="18" cy="18" r="16" fill="none" stroke="#0b6b3a" stroke-width="2"/><path d="M11 10h14M11 26h14M12 10l12 16M24 10L12 26" stroke="#0b6b3a" stroke-width="2" fill="none"/></svg>
      <span><strong style="display:inline">Easement</strong> valuations</span>
    </div>
    <div class="purpose" style="left:295px;top:760px">
      <svg class="icon-ring" viewBox="0 0 36 36"><circle cx="18" cy="18" r="16" fill="none" stroke="#0b6b3a" stroke-width="2"/><rect x="12" y="9" width="12" height="17" rx="1.5" fill="none" stroke="#0b6b3a" stroke-width="1.8"/><path d="M15 14h6M15 18h6M15 22h4" stroke="#0b6b3a" stroke-width="1.4"/></svg>
      <span><strong>Wills and probate</strong>Valuations</span>
    </div>
    <div class="purpose" style="left:295px;top:810px">
      <svg class="icon-ring" viewBox="0 0 36 36"><circle cx="18" cy="18" r="16" fill="none" stroke="#0b6b3a" stroke-width="2"/><path d="M11 15l3-5h8l3 5-7 11z M11 15h14M16 10l-1.5 5L18 26M20 10l1.5 5L18 26" stroke="#0b6b3a" stroke-width="1.5" fill="none"/></svg>
      <span><strong>Insolvency/asset</strong>Realisation valuations</span>
    </div>
  </div>

  <div class="page page--right types">
    <div class="abs grid-rule-v"></div>
    <div class="abs grid-rule-h"></div>

    <div class="photo" role="img" aria-label="White residential apartment buildings under blue sky" style="left:34px;top:32px;width:229px;height:181px;background:linear-gradient(180deg,#9fc3e2 0%,#e9eef2 50%,#7d8f6a 100%)"></div>
    <h3 class="type__head" style="left:34px;top:232px"><b>Residential</b> valuations</h3>
    <div class="type__rule" style="left:34px;top:252px;width:229px"></div>
    <p class="type__copy" style="left:34px;top:260px">Brookmere valuers provide valuation and advisory to individuals, businesses and financial institutions to assist and add value to all areas of residential investment, being for stamp duty, mortgage, tax or family law related purposes.</p>
    <ul class="bullets" style="left:34px;top:352px">
      <li class="g">Residential houses</li><li class="g">Off-the-plan units</li>
      <li class="k">Vacant land</li><li class="k">Prestige homes</li>
      <li class="g">Apartments</li><li class="g">Duplex sites</li>
      <li class="k">Townhouses &amp; villa homes</li><li class="k">Heritage-listed properties</li>
    </ul>

    <div class="photo" role="img" aria-label="Large empty industrial warehouse interior with blue steel roof" style="left:311px;top:32px;width:229px;height:181px;background:linear-gradient(180deg,#2a6fa8 0%,#5d9ccc 50%,#cfe3ef 100%)"></div>
    <h3 class="type__head" style="left:311px;top:232px"><b>Industrial</b> valuations</h3>
    <div class="type__rule" style="left:311px;top:252px;width:229px"></div>
    <p class="type__copy" style="left:311px;top:260px">Brookmere valuers provide valuation and advisory to individuals, governments, institutions and investors. We assist in all areas of industrial valuations, from small-scale industrial strata units, to large, freestanding industrial buildings.</p>
    <ul class="bullets" style="left:311px;top:352px">
      <li class="g">Strata titled industrial units</li><li class="g">Workshops</li>
      <li class="k">Freehold industrial buildings</li><li class="k">Vacant industrial development sites</li>
      <li class="k" style="visibility:hidden">&nbsp;</li><li class="g">Self-storage facilities</li>
    </ul>

    <div class="photo" role="img" aria-label="Glass office towers seen from below against a cloudy sky" style="left:28px;top:479px;width:229px;height:181px;background:linear-gradient(180deg,#4b86c4 0%,#b9d4ec 45%,#1f4f7f 100%)"></div>
    <h3 class="type__head" style="left:28px;top:678px"><b>Commercial</b> valuations</h3>
    <div class="type__rule" style="left:28px;top:698px;width:229px"></div>
    <p class="type__copy" style="left:28px;top:705px">Brookmere valuers provide valuation and advisory to individuals, businesses and financial institutions to assist and add value to all areas of office investment, including those for stamp duty, mortgage, tax, or family-law related purposes.</p>
    <ul class="bullets" style="left:28px;top:797px">
      <li class="g">Strata titled office suites</li><li class="g">Freehold commercial buildings</li>
      <li class="k">Medical suites</li>
    </ul>

    <div class="photo" role="img" aria-label="Multi-level shopping centre interior with shopfronts" style="left:311px;top:479px;width:229px;height:181px;background:linear-gradient(180deg,#d9d4cc 0%,#a89a8a 50%,#e3dfd8 100%)"></div>
    <h3 class="type__head" style="left:311px;top:678px"><b>Retail</b> valuations</h3>
    <div class="type__rule" style="left:311px;top:698px;width:229px"></div>
    <p class="type__copy" style="left:311px;top:705px">Brookmere valuers provide valuation and advisory to individuals, businesses and financial institutions to assist and add value to all areas of retail investment, being for stamp duty, mortgage, tax or family law related purposes.</p>
    <ul class="bullets" style="left:311px;top:797px">
      <li class="g">Strata titled retail suites</li><li class="g">Freehold retail buildings</li>
      <li class="k">Mixed use retail /residential buildings</li>
    </ul>

    <svg class="abs" style="left:0;top:0" width="570" height="880" viewBox="0 0 570 880">
      <g fill="none" stroke="#fff" stroke-width="4" stroke-linecap="round">
        <path d="M46 160 V190 Q46 202 58 202 H150"/>
        <path d="M323 160 V190 Q323 202 335 202 H430"/>
        <path d="M40 607 V637 Q40 649 52 649 H145"/>
        <path d="M323 607 V637 Q323 649 335 649 H430"/>
      </g>
    </svg>
  </div>
</section>

</body>
</html>
```